Garden Design Flier

I would like a PDF of this half page A4 flier in soft green tones with dark green leaves.

Target Market(s)

Home owners and real estate agents

Font styles to use
Serif
Other font styles liked:
• Papyrus

Colors
acd136
9bcb3c
cadf82
fefdec

Requirements
Must have
• Green tones
Nice to have
• Leaves, vines, lawns
Should not have
• Open to ideas, but classic style

```html
<!DOCTYPE html>
<html lang="en">
<head>
<meta charset="utf-8">
<title>Verdane Gardens – Flier</title>
<link href="https://fonts.googleapis.com/css2?family=Alegreya:wght@400;700&family=Alegreya+Sans:wght@500&display=swap" rel="stylesheet">
<style>
  :root {
    --page-bg: #ffffff;
    --flier-light: #cfe5b4;
    --flier-mid: #a9cf8a;
    --flier-deep: #94bd78;
    --leaf-dark: #3f7f4f;
    --leaf-mid: #6aa86a;
    --ink: #141a12;
    --title-white: #ffffff;
  }
  html, body {
    margin: 0;
    width: 1200px;
    height: 1000px;
    overflow: hidden;
    background: var(--page-bg);
  }
  .flier {
    position: absolute;
    left: 341px;
    top: 150px;
    width: 504px;
    height: 715px;
    overflow: hidden;
    background:
      radial-gradient(ellipse at 20% 75%, rgba(230,242,210,0.7), transparent 45%),
      radial-gradient(ellipse at 85% 55%, rgba(215,235,190,0.6), transparent 40%),
      linear-gradient(180deg, var(--flier-light) 0%, var(--flier-mid) 55%, var(--flier-deep) 100%);
    font-family: "Alegreya", Georgia, serif;
    color: var(--ink);
  }
  .leaf-canopy {
    position: absolute;
    left: 0;
    top: 0;
    width: 504px;
    height: 340px;
    background:
      radial-gradient(ellipse at 25% 15%, var(--leaf-dark), transparent 55%),
      radial-gradient(ellipse at 75% 20%, var(--leaf-mid), transparent 55%),
      radial-gradient(ellipse at 50% 70%, rgba(80,140,85,0.55), transparent 50%),
      linear-gradient(180deg, rgba(100,160,100,0.85) 0%, rgba(169,207,138,0) 100%);
  }
  .brand-name {
    position: absolute;
    left: 0;
    width: 504px;
    text-align: center;
    color: var(--title-white);
    font-weight: 400;
    line-height: 1;
    margin: 0;
  }
  .brand-name__top { top: 122px; font-size: 90px; letter-spacing: 1px; }
  .brand-name__bottom { top: 212px; font-size: 104px; }
  .credit {
    position: absolute;
    right: 48px;
    top: 328px;
    text-align: right;
    line-height: 1;
  }
  .credit__name { font-size: 15px; }
  .credit__qual {
    font-family: "Alegreya Sans", Arial, sans-serif;
    font-weight: 500;
    font-size: 12.5px;
    margin-top: 2px;
  }
  .content {
    position: absolute;
    left: 97px;
    top: 392px;
    width: 310px;
    text-align: center;
  }
  .tagline {
    font-size: 19px;
    font-weight: 700;
    margin: 0 0 14px;
  }
  .blurb {
    font-size: 16px;
    line-height: 18px;
    text-align: justify;
    text-align-last: center;
    margin: 0 0 17px;
  }
  .contact {
    font-size: 21px;
    line-height: 20px;
    margin: 6px 0 0;
  }
  .abn {
    font-size: 14px;
    margin-top: 30px;
  }
</style>
</head>
<body>
  <div class="flier">
    <div class="leaf-canopy" role="img" aria-label="Photograph of green maple leaves hanging across the top of the flier"></div>

    <h1 class="brand-name brand-name__top">VERDANE</h1>
    <div class="brand-name brand-name__bottom">gardens</div>

    <div class="credit">
      <div class="credit__name">by LIAM HARTWELL</div>
      <div class="credit__qual">Certificate 3. Horticulture Northvale College</div>
    </div>

    <div class="content">
      <h2 class="tagline">Design Install Grow Tend Enjoy</h2>
      <p class="blurb">All your gardening and landscaping needs from design and installation to general maintenance.</p>
      <p class="blurb">Bespoke vegetable gardens and potager designs created to suite your site and requirements.</p>
      <p class="contact">liam@verdanegardens.com.au<br>mobile: 0400-218365</p>
      <div class="abn">ABN: 51902736418</div>
    </div>
  </div>
</body>
</html>
```